Borstad-Lyngmo International AS

We need a design for our company including background pictures on our web (wix-template), redesign of logo and reports. Our company delivers personality test and services to clients when hiring staff or related to organizatonal developement.

Target Market(s)

Unisex, Age 30-50, managers in private corporations

Industry/Entity Type

Recruitment

Logo Text

Bygger laget sterkt (english translate: buids your team strong)

Number of Pages Required

1 page

Font styles to use
Sans Serif

Colors
add136
34a6d7
0255a3

Requirements
Must have
• The ideal designer will be the one to bring my narrative come to life. And it will have to include the testresults report and redesign (!) of my logo. Following the attached brief in ppt:
• - the testresult report
• - redesign logo
• - graphic elements in a maritime narrative
• - including the boat, the radar, 4 WINDs, the compass etc
Nice to have
• A strong narrative with a lot of elements.
• I really like the green color in the attached breif ;-)

```html
<!DOCTYPE html>
<html lang="en">
<head>
<meta charset="utf-8">
<title>Borstad-Lyngmo International</title>
<link href="https://fonts.googleapis.com/css2?family=Lato:wght@300;400;700&display=swap" rel="stylesheet">
<style>
  :root {
    --blue: #1a7fc8;
    --blue-text: #1577c2;
    --ink: #222;
    --body-text: #666;
    --rule: #d9d9d9;
    --box-line: #c9c9c9;
    --footer-bg: #e3e3e3;
    --white: #fff;
  }
  * { margin: 0; padding: 0; box-sizing: border-box; }
  html, body { width: 1200px; height: 2799px; overflow: hidden; }
  body { position: relative; background: var(--white); font-family: 'Lato', sans-serif; color: var(--ink); }

  .hero {
    position: absolute; left: 0; top: 0; width: 1200px; height: 579px;
    background: linear-gradient(100deg, #2f3238 0%, #3e4147 40%, #4b4d52 65%, #2c2e33 100%);
  }
  .brand { position: absolute; left: 168px; top: 40px; display: flex; align-items: center; gap: 16px; }
  .brand-square { width: 56px; height: 56px; background: var(--white); }
  .brand-name { color: var(--white); font-weight: 700; font-size: 17px; line-height: 22px; }

  .main-nav {
    position: absolute; left: 549px; top: 43px; height: 40px;
    display: flex; border: 1.5px solid rgba(255,255,255,.85);
  }
  .main-nav a {
    color: var(--white); text-decoration: none; font-size: 14px; font-weight: 400;
    display: flex; align-items: center; padding: 0 18px;
    border-right: 1.5px solid rgba(255,255,255,.85);
  }
  .main-nav a:last-child { border-right: none; padding-right: 34px; }

  .hero-title {
    position: absolute; left: 162px; top: 254px; width: 520px;
    color: var(--white); font-weight: 300; font-size: 31px; line-height: 48px;
  }

  .intro-box {
    position: absolute; left: 170px; top: 511px; width: 858px; height: 417px;
    border: 2px solid var(--blue); background: transparent;
    padding: 118px 0 0 108px;
  }
  .section-heading { color: var(--blue-text); font-size: 21px; font-weight: 400; letter-spacing: .3px; }
  .intro-box p { margin-top: 20px; width: 620px; font-size: 16px; line-height: 33px; color: var(--body-text); }

  .handshake-photo {
    position: absolute; left: 0; top: 993px; width: 1200px; height: 444px;
    background: linear-gradient(100deg, #e88a1e 0%, #f2b066 22%, #e9e9e7 45%, #dcdcda 65%, #b9b7b2 85%, #8f8a84 100%);
  }

  .services { position: absolute; left: 181px; top: 1520px; width: 847px; }
  .services .section-heading { margin-left: 17px; }
  .service-row { display: flex; padding: 34px 0 32px 17px; }
  .service-row + .service-row { border-top: 1.5px solid var(--rule); padding-top: 50px; padding-bottom: 24px; }
  .service-name { width: 168px; font-size: 16px; line-height: 20px; color: #555; text-transform: uppercase; }
  .service-text { width: 640px; font-size: 16px; line-height: 31px; color: var(--body-text); margin-top: -6px; }
  .learn-more { display: block; margin-left: 20px; margin-top: 6px; color: var(--blue-text); font-size: 15px; text-decoration: none; }

  .styles-band {
    position: absolute; left: 0; top: 1913px; width: 1200px; height: 428px;
    background: var(--blue); color: var(--white); padding: 82px 0 0 198px;
  }
  .styles-band h2 { font-size: 21px; font-weight: 400; }
  .styles-band h3 { font-size: 19px; font-weight: 400; margin: 40px 0 0 8px; }
  .styles-list { list-style: none; margin: 10px 0 0 4px; }
  .styles-list li { font-size: 14px; line-height: 33px; }
  .styles-list li::before { content: "»"; margin-right: 8px; }

  .contact-heading { position: absolute; left: 175px; top: 2392px; font-size: 21px; font-weight: 400; color: var(--ink); }
  .contact-box {
    position: absolute; left: 177px; top: 2448px; width: 851px; height: 191px;
    border: 1.5px solid var(--box-line); display: flex;
  }
  .contact-col { padding: 36px 0 0 52px; }
  .contact-col:nth-child(1) { width: 267px; border-right: 1.5px solid var(--box-line); }
  .contact-col:nth-child(2) { width: 286px; border-right: 1.5px solid var(--box-line); padding-left: 76px; }
  .contact-col:nth-child(3) { flex: 1; padding-left: 66px; }
  .contact-col h4 { color: var(--blue-text); font-size: 18px; font-weight: 400; margin-bottom: 12px; }
  .contact-col p { font-size: 12px; line-height: 25px; color: var(--ink); }
  .social-links { display: flex; gap: 6px; margin-top: -2px; }
  .social-links span { width: 29px; height: 29px; border: 1.5px solid var(--ink); border-radius: 50%; }

  .site-footer {
    position: absolute; left: 0; top: 2726px; width: 1200px; height: 73px;
    background: var(--footer-bg); border-top: 1px solid #cfcfcf;
  }
  .site-footer p { position: absolute; left: 752px; top: 26px; font-size: 11px; color: #555; }
</style>
</head>
<body>
  <header class="hero" role="img" aria-label="Dimmed photo of two colleagues working together at a laptop">
    <div class="brand">
      <div class="brand-square"></div>
      <div class="brand-name">Borstad-Lyngmo<br>International</div>
    </div>
    <nav class="main-nav">
      <a href="#">Home</a>
      <a href="#">About Us</a>
      <a href="#">Product</a>
      <a href="#">Jobs</a>
      <a href="#">Contact Us</a>
    </nav>
    <h1 class="hero-title">Curabitur vel mi sit amet magna malesuada ultrices Ut nisi erat fermentum vel congue</h1>
  </header>

  <section class="intro-box">
    <h2 class="section-heading">WHO WE ARE</h2>
    <p>Borstad-Lyngmo International is a company founded in Oslo, Norway. We sell personality tests. New owners is aiming to turn the business around with a more compelling design, new features and an active sales offensive.</p>
  </section>

  <div class="handshake-photo" role="img" aria-label="Top-down photo of two people shaking hands across a desk"></div>

  <section class="services">
    <h2 class="section-heading">OUR SERVICES</h2>
    <div class="service-row">
      <div class="service-name">Personality<br>test</div>
      <div class="service-text">We offer a personality test originally derived from Halvorsen and Brandt's studies in the US market in the 70'ies.</div>
    </div>
    <div class="service-row">
      <div class="service-name">Answering<br>questions</div>
      <div class="service-text">From answering 120 questions any candidate will be "measure" to fit a set of specific required traits. Basically ego-drive and empathy.</div>
    </div>
    <a class="learn-more" href="#">LEARN MORE</a>
  </section>

  <section class="styles-band">
    <h2>PERSONALITY TEST</h2>
    <h3>4 DIFFERENT WORKING STYLES</h3>
    <ul class="styles-list">
      <li>In an effort to simplify we downscale the never ending diversity in 4 architypes.</li>
      <li>All 4 styles have equal importance</li>
      <li>Everyone can have more than one style, but not at the same time!</li>
      <li>A Metaphor can be the 4 wind (north, south, east and west)</li>
    </ul>
  </section>

  <h2 class="contact-heading">CONTACT US</h2>
  <section class="contact-box">
    <div class="contact-col">
      <h4>CONTACT</h4>
      <p>Email: post@borstadlyngmo.example<br>Phone: 555-010-2040<br>Fax: 555-010-2041</p>
    </div>
    <div class="contact-col">
      <h4>LOCATION</h4>
      <p>42 Harbour Lane #4B<br>Bergen 5003 NO</p>
    </div>
    <div class="contact-col">
      <h4>FOLLOW US</h4>
      <div class="social-links"><span></span><span></span><span></span><span></span></div>
    </div>
  </section>

  <footer class="site-footer">
    <p>© 2017 Company Name &nbsp;All right reserved &nbsp;Terms of Use</p>
  </footer>
</body>
</html>
```